Marquise Velvet Stable Goods - Elite line of horse care grooming products

I wanted to have a label design for my equestrian products that made the people who use them on their horses feel like a princess. I use all natural ingredients, they smell wonderful and work! I think my current design could be more amazing.... I have a total of 6 products. The final design should communicate that you are using the finest and highest quality ingredients on your best friend. please see my website (www.MarquiseStable.example) for the design aesthetic I'm going for. Design Guide:
The design should communicate that you are using the finest and highest quality ingredients on your best friend.
Create a bold, unique, visually-appealing design
Make buyer feel like a princess
Impart that you are taking care of your horse because you’re buying the best
Stand out from most other products currently on the market that look boring/outdated, bland
Avoid any design or visual images that impart chemical, industrial or commercial connotations
Key Terms: Elite, Bold, Serious, Baroque elegance, Feminine, Elegance, Wow, Fairytale, Fantasy, Elegance,

Please create: Design separate front and back BOPP labels for 32oz. spray bottle, 3.5x5” Rosemary, Lavender & Mint Insect Repellent

Design should convey a sense of wealth and prestige
Elegance & sophistication
Professional quality

Design Guide:

Key Attributes of Product:
Expensive product
Therapeutic-grade essential oils
All-natural ingredients
No poisons or pesticides
Smell wonderful
They work

Please use royal purple and gold

Target Market(s)

High end female horse owners..12-65yo female horse owners who want to and can afford to buy premium products for horse grooming.

Font styles to use
Sans Serif
Decorative
Script

Colors
876aae

Requirements
Must have
• Elegance, wow, pick me. Mandatory Graphics:
• Marquise Velvet Stable Goods logo with gold doily (no gradient on gold)
Nice to have
• Fairytale, fantasy, quality, elite, smells good,
Should not have
• I do not want my bottles to look like pesticides or poison.

```html
<!DOCTYPE html>
<html lang="en">
<head>
<meta charset="utf-8">
<title>Marquise Velvet Stable Goods – Natural Insect Repellent Label</title>
<link href="https://fonts.googleapis.com/css2?family=Pinyon+Script&family=Playfair+Display:wght@400&family=Montserrat:wght@400&family=Didact+Gothic&display=swap" rel="stylesheet">
<style>
  :root {
    --royal-purple: #4a1679;
    --label-white: #f8f6fa;
    --gold: #c49a52;
    --page: #ffffff;
    --ink: #2a2130;
  }
  html, body {
    margin: 0;
    padding: 0;
    width: 1200px;
    height: 1200px;
    overflow: hidden;
    background: var(--page);
  }
  .canvas {
    position: relative;
    width: 1200px;
    height: 1200px;
  }
  .label {
    position: absolute;
    left: 255px;
    top: 36px;
    width: 690px;
    height: 1128px;
    background: var(--label-white);
    border-top: 5px solid var(--gold);
    border-bottom: 5px solid var(--gold);
    box-sizing: border-box;
    text-align: center;
    color: var(--royal-purple);
  }
  .brand {
    position: absolute;
    top: 80px;
    left: 0;
    width: 100%;
    display: flex;
    flex-direction: column;
    align-items: center;
  }
  .brand-circle {
    width: 200px;
    height: 200px;
    border-radius: 50%;
    border: 4px solid var(--gold);
    box-sizing: border-box;
  }
  .brand-name {
    margin-top: 18px;
    font-family: "Didact Gothic", sans-serif;
    font-size: 28px;
    color: var(--royal-purple);
    letter-spacing: 1px;
  }
  .title-script {
    position: absolute;
    top: 400px;
    left: 0;
    width: 100%;
    font-family: "Pinyon Script", cursive;
    font-size: 160px;
    line-height: 1;
    color: var(--royal-purple);
  }
  .title-main {
    position: absolute;
    top: 618px;
    left: 0;
    width: 100%;
    font-family: "Playfair Display", serif;
    font-size: 76px;
    line-height: 1;
    letter-spacing: -2px;
    color: var(--royal-purple);
  }
  .blend {
    position: absolute;
    top: 726px;
    left: 0;
    width: 100%;
    font-family: "Montserrat", sans-serif;
    font-size: 23px;
    color: var(--ink);
    letter-spacing: 0.5px;
  }
  .description {
    position: absolute;
    top: 798px;
    left: 60px;
    width: 570px;
    margin: 0;
    font-family: "Didact Gothic", sans-serif;
    font-size: 28px;
    line-height: 35px;
    color: var(--ink);
  }
  .tagline {
    position: absolute;
    top: 998px;
    left: 0;
    width: 100%;
    font-family: "Pinyon Script", cursive;
    font-size: 60px;
    line-height: 1;
    color: var(--royal-purple);
    word-spacing: 18px;
  }
</style>
</head>
<body>
  <main class="canvas">
    <section class="label">
      <div class="brand">
        <div class="brand-circle"></div>
        <div class="brand-name">Marquise Velvet Stable Goods</div>
      </div>
      <div class="title-script">Natural</div>
      <h1 class="title-main" style="margin:0;font-weight:400;">Insect Repellent</h1>
      <div class="blend">LAVENDER, MINT &amp; ROSEMARY BLEND</div>
      <p class="description">Natural ingredients made with<br>therapeutic grade essential oils!<br>Free of harsh chemicals, lovely smell.<br>Safe for humans too...go ahead,<br>spray it on yourself!</p>
      <div class="tagline">Love your horse!</div>
    </section>
  </main>
</body>
</html>
```